Webdesign plus CSS for a German company data register

We need a unique and attractive webdesign including CSS development for a website (https://kontorblick.de/) of our newly founded company. We collect company data from several public registers to display them aggregated.

Your design should communicate science, data security, a business note and perhaps a slice of nerdness. Elements - like color and layout - of our logo should also be found in your design.

Target Market(s)

banks, insurance companies, authorities etc.

Industry/Entity Type

Internet

Coding

Coded - Design and coding required

Number of Pages Required

3 page

Font styles to use
Sans Serif

Requirements
Must have
• mockups, CSS

eye catching, easy to read / navigate
Nice to have
• pictogramms / logos for essential content

```html
<!DOCTYPE html>
<html lang="de">
<head>
<meta charset="utf-8">
<title>Statistiken – Kontorblick</title>
<link rel="stylesheet" href="https://fonts.googleapis.com/css2?family=Open+Sans:wght@400;600;700&display=swap">
<style>
  :root {
    --orange: #ff5a0a;
    --charcoal: #4f4f4f;
    --ink: #333333;
    --text: #3d3d3d;
    --white: #ffffff;
    --shadow: rgba(0, 0, 0, 0.14);
  }
  * { box-sizing: border-box; margin: 0; padding: 0; }
  html, body {
    width: 1200px;
    height: 889px;
    overflow: hidden;
    background: var(--white);
    font-family: "Open Sans", Arial, sans-serif;
    color: var(--text);
  }
  .page { position: relative; width: 1200px; height: 889px; }

  /* Header */
  .site-header {
    position: absolute; top: 0; left: 0; width: 1200px; height: 45px;
    background: var(--white);
    box-shadow: 0 1px 4px var(--shadow);
    z-index: 2;
  }
  .corner-accent { position: absolute; top: 0; left: 0; }
  .brand {
    position: absolute; left: 158px; top: 13px;
    font-size: 14px; font-weight: 700; color: var(--orange);
    letter-spacing: 0.3px; text-decoration: none;
  }
  .main-nav { position: absolute; top: 0; left: 669px; height: 45px; }
  .main-nav a {
    position: absolute; top: 13px;
    font-size: 11px; font-weight: 600; letter-spacing: 1px;
    color: var(--ink); text-decoration: none; white-space: nowrap;
  }
  .main-nav .is-active::after {
    content: ""; position: absolute; left: -5px; right: -4px; top: 19px;
    height: 2px; background: var(--orange);
  }
  .contact-button {
    position: absolute; left: 956px; top: 9px; width: 87px; height: 27px;
    background: var(--orange); color: var(--white);
    font-size: 12px; line-height: 27px; text-align: center; text-decoration: none;
    box-shadow: 0 1px 3px var(--shadow);
  }
  .lang-switch {
    position: absolute; left: 1090px; top: 14px;
    font-size: 11px; font-weight: 600; color: var(--ink);
  }
  .lang-switch svg { margin-left: 4px; vertical-align: 1px; }

  /* Title */
  .page-title {
    position: absolute; top: 125px; left: 0; width: 1200px;
    text-align: center; font-size: 24px; font-weight: 600;
    letter-spacing: 0.8px; color: var(--ink);
  }
  .page-title .accent { color: var(--orange); }

  /* Stat cards */
  .stat-card {
    position: absolute; top: 232px; width: 288px; height: 223px;
    border: 1px solid var(--orange);
    box-shadow: 0 1px 4px var(--shadow);
  }
  .stat-card--companies { left: 124px; }
  .stat-card--people { left: 456px; }
  .stat-card--founded { left: 794px; }
  .stat-card__title {
    position: absolute; top: -17px; left: 18px; width: 250px; height: 37px;
    background: var(--white); box-shadow: 0 1px 4px var(--shadow);
    font-size: 16px; font-weight: 400; letter-spacing: 0.5px;
    line-height: 37px; text-align: center; color: var(--text); white-space: nowrap;
  }
  .stat-card__list { list-style: none; position: absolute; top: 38px; left: 28px; }
  .stat-card__list li { font-size: 10px; height: 31px; color: var(--ink); }

  /* Privacy band */
  .privacy-band {
    position: absolute; top: 676px; left: 0; width: 1200px; height: 47px;
    background: var(--charcoal); color: var(--white);
    font-size: 11px; font-weight: 700; letter-spacing: 0.8px;
    line-height: 45px; text-align: center;
  }
  .privacy-band a { color: var(--orange); text-decoration: none; margin-left: 8px; }

  /* Footer */
  .site-footer { position: absolute; top: 856px; left: 0; width: 1200px; font-size: 10px; }
  .site-footer span, .site-footer a { position: absolute; white-space: nowrap; }
  .copyright { left: 414px; color: var(--text); }
  .site-footer a { color: var(--orange); text-decoration: none; }
  .footer-imprint { left: 646px; }
  .footer-privacy { left: 733px; }
</style>
</head>
<body>
<div class="page">
  <header class="site-header">
    <svg class="corner-accent" width="118" height="45" viewBox="0 0 118 45" aria-hidden="true">
      <polygon points="0,0 44,0 82,45 0,45" fill="#ff5a0a"/>
      <polygon points="44,0 78,0 117,45 82,45" fill="#4f4f4f"/>
    </svg>
    <a class="brand" href="https://kontorblick.de/">Kontorblick</a>
    <nav class="main-nav">
      <a href="#" style="left:0">Start</a>
      <a href="#" style="left:50px">Firmen</a>
      <a href="#" style="left:114px">Personen</a>
      <a href="#" class="is-active" style="left:194px">Statistiken</a>
    </nav>
    <a class="contact-button" href="#">Kontakt</a>
    <div class="lang-switch">DE<svg width="8" height="5" viewBox="0 0 8 5"><polygon points="0,0 8,0 4,5" fill="#333"/></svg></div>
  </header>

  <h1 class="page-title">Statistiken in <span class="accent">Kontorblick</span></h1>

  <section class="stat-card stat-card--companies">
    <h2 class="stat-card__title">Am meisten besuchte Firmen</h2>
    <ul class="stat-card__list"><li>Firmen 1</li><li>Firmen 2</li><li>Firmen 3</li></ul>
  </section>
  <section class="stat-card stat-card--people">
    <h2 class="stat-card__title">Am meisten besuchte Personen</h2>
    <ul class="stat-card__list" style="left:27px"><li>Personen 1</li><li>Personen 2</li><li>Personen 3</li></ul>
  </section>
  <section class="stat-card stat-card--founded">
    <h2 class="stat-card__title">Die neusten Gründungen</h2>
    <ul class="stat-card__list"><li>Gründun 1</li><li>Gründun 2</li><li>Gründun 3</li></ul>
  </section>

  <div class="privacy-band">Datenschutz steht bei uns an erster Stelle. sehen <a href="#">Datenschutz</a></div>

  <footer class="site-footer">
    <span class="copyright">© 2020 - Kontorblick</span>
    <a class="footer-imprint" href="#">Impressum</a>
    <a class="footer-privacy" href="#">Datenschutz</a>
  </footer>
</div>
</body>
</html>
```